Vell Partners Building Business Cards

We need a business card that reflects our business as "Solar Experts" in San Diego. Browse our website www.vellpartners.example our License needs to be displayed as "CSLB# 4718392" our phone number is (619) 555-0147

Save thousands on your electric bills and increase the value of your home while helping to protect the environment. Our solar installation experts will help you design the system that's right for you, using only the highest quality equipment that will look great and give you ideal performance. Our goal is to make you energy independent, and get your electric bill to 0.

Tobias Wrenfield
(619) 555-0147
tobias@vellpartners.example

Target Market(s)

Home owners in san diego looking for solar

Industry/Entity Type

Solar Energy

Contact Information for Business Card

Tobias Wrenfield
(619) 555-0147
tobias@vellpartners.example

Font styles to use
Other font styles liked:
• Use our logo font

Requirements
Must have
• License needs to be displayed as "CSLB# 4718392" our phone number is (619) 555-0147
Nice to have
• Real images of rooftop home solar in san diego
Should not have
• our business address

```html
<!DOCTYPE html>
<html lang="en">
<head>
<meta charset="utf-8">
<title>Vell Partners Building – Business Card</title>
<link rel="stylesheet" href="https://fonts.googleapis.com/css2?family=Montserrat:wght@700;800&family=Cinzel:wght@400;500&display=swap">
<style>
  :root {
    --page-bg: #1b1c1f;
    --card-blue: #1d4d8c;
    --sun-gold: #f6b31c;
    --ink-white: #ffffff;
    --ink-navy: #143a6b;
    --sky-top: #5d7fa6;
    --panel-blue: #243a63;
    --roof-grey: #7d7a73;
  }
  * { box-sizing: border-box; margin: 0; padding: 0; }
  html, body { width: 1200px; height: 900px; overflow: hidden; background: var(--page-bg); }
  .canvas {
    width: 1200px; height: 900px;
    display: flex; flex-direction: column; align-items: center; justify-content: center; gap: 30px;
  }
  .card {
    position: relative; width: 700px; height: 400px; overflow: hidden;
    box-shadow: 0 10px 30px rgba(0,0,0,.5);
  }

  /* Front */
  .card-front .rooftop-photo {
    position: absolute; inset: 0;
    background:
      linear-gradient(160deg, rgba(93,127,166,.9) 0%, rgba(36,58,99,.95) 40%, rgba(30,48,84,1) 65%, rgba(125,122,115,.9) 100%),
      var(--panel-blue);
  }
  .card-front .brand-name {
    position: absolute; left: 90px; top: 150px;
    font-family: "Montserrat", sans-serif; font-weight: 800; font-size: 46px;
    color: var(--ink-white); letter-spacing: -0.5px; line-height: 1.05;
  }
  .card-front .gold-rule {
    position: absolute; left: 0; right: 0; bottom: 52px; height: 2px; background: var(--sun-gold);
  }
  .card-front .gold-rule-short {
    position: absolute; left: 430px; right: 0; top: 250px; height: 2px; background: var(--sun-gold);
  }
  .card-front .web-address {
    position: absolute; right: 40px; bottom: 62px;
    font-family: "Cinzel", serif; font-size: 15px; color: var(--ink-white); letter-spacing: 1px;
  }

  /* Back */
  .card-back { background: var(--card-blue); }
  .card-back .brand-mark {
    position: absolute; left: 60px; top: 120px;
    display: flex; align-items: center; gap: 16px;
  }
  .card-back .brand-mark .dot {
    width: 56px; height: 56px; border-radius: 50%; background: var(--sun-gold); flex: none;
  }
  .card-back .brand-mark .brand-name {
    font-family: "Montserrat", sans-serif; font-weight: 800; font-size: 26px;
    color: var(--ink-white); line-height: 1.1; width: 240px;
  }
  .card-back .name-bar {
    position: absolute; right: 0; top: 110px; width: 280px; height: 48px;
    background: var(--sun-gold);
    display: flex; align-items: center; padding-left: 22px;
    font-family: "Montserrat", sans-serif; font-weight: 700; font-size: 21px; color: var(--ink-navy);
  }
  .card-back .license {
    position: absolute; right: 30px; top: 180px;
    font-family: "Cinzel", serif; font-size: 17px; color: var(--ink-white); letter-spacing: .5px;
  }
  .card-back .license-rule {
    position: absolute; left: 380px; right: 220px; top: 193px; height: 2px; background: var(--sun-gold);
  }
  .card-back .contact-list {
    position: absolute; left: 60px; top: 262px; list-style: none;
    font-family: "Cinzel", serif; font-size: 16px; color: var(--ink-white); letter-spacing: .5px;
  }
  .card-back .contact-list li { display: flex; align-items: center; gap: 10px; height: 26px; }
  .card-back .contact-list svg { width: 13px; height: 13px; fill: var(--sun-gold); flex: none; }
  .card-back .bottom-rule {
    position: absolute; left: 60px; right: 60px; bottom: 40px; height: 2px; background: var(--sun-gold);
  }
</style>
</head>
<body>
<main class="canvas">

  <section class="card card-front">
    <div class="rooftop-photo" role="img" aria-label="Photo of solar panels installed on a tiled home rooftop in San Diego"></div>
    <div class="brand-name">Vell Partners<br>Building</div>
    <div class="gold-rule-short"></div>
    <div class="web-address">www.vellpartners.example</div>
    <div class="gold-rule"></div>
  </section>

  <section class="card card-back">
    <div class="brand-mark">
      <span class="dot"></span>
      <span class="brand-name">Vell Partners Building</span>
    </div>
    <div class="name-bar">Tobias Wrenfield</div>
    <div class="license-rule"></div>
    <div class="license">CSLB# 4718392</div>
    <ul class="contact-list">
      <li>
        <svg viewBox="0 0 24 24" aria-hidden="true"><path d="M6.6 10.8a15.1 15.1 0 0 0 6.6 6.6l2.2-2.2a1 1 0 0 1 1-.25 11.4 11.4 0 0 0 3.6.57 1 1 0 0 1 1 1V20a1 1 0 0 1-1 1A17 17 0 0 1 3 4a1 1 0 0 1 1-1h3.5a1 1 0 0 1 1 1c0 1.25.2 2.45.57 3.57a1 1 0 0 1-.25 1z"/></svg>
        (619) 555-0147
      </li>
      <li>
        <svg viewBox="0 0 24 24" aria-hidden="true"><path d="M2 5h20v14H2z M4 7v.5l8 5 8-5V7l-8 5z" fill-rule="evenodd"/></svg>
        tobias@vellpartners.example
      </li>
      <li>
        <svg viewBox="0 0 24 24" aria-hidden="true"><circle cx="12" cy="12" r="10"/></svg>
        www.vellpartners.example
      </li>
    </ul>
    <div class="bottom-rule"></div>
  </section>

</main>
</body>
</html>
```